Bref créative
DRK Business Card
Modern
Lou Ferrand
418B Quarry Gate Rd
Harlow Point, MD 21870
lou@drkhvc.com
www.drkhvc.com
(see the bullet points on our existing business card and try to incorporate them)
Attached is our previous card. The services offered should be incorporated into the new card.
I can get an AI file of this logo if needed. Let me know.

```html
<!DOCTYPE html>
<html lang="en">
<head>
<meta charset="utf-8">
<title>DRK Business Card – Lou Ferrand</title>
<link rel="stylesheet" href="https://fonts.googleapis.com/css2?family=Source+Sans+3:wght@400;600;700&display=swap">
<style>
  :root {
    --page: #ffffff;
    --frame: #c9c9c9;
    --band-deep: #16248a;
    --band-mid: #1f4fb8;
    --band-light: #3a86e0;
    --swoosh-light: #f2f2f2;
    --swoosh-dark: #9a9a9a;
    --contact-text: #ffffff;
    --name-text: #26288c;
    --brand-text: #1f5fc0;
  }
  * { margin: 0; padding: 0; box-sizing: border-box; }
  html, body {
    width: 1200px;
    height: 703px;
    overflow: hidden;
    background: var(--page);
  }
  .business-card {
    position: relative;
    width: 1200px;
    height: 703px;
    background: var(--page);
    border: 2px solid var(--frame);
    font-family: "Source Sans 3", "Myriad Pro", Arial, sans-serif;
  }
  .card-face {
    position: absolute;
    inset: 10px;
    border: 2px solid var(--frame);
    overflow: hidden;
    background: var(--page);
  }
  .header-band {
    position: absolute;
    left: 0;
    top: 0;
    width: 100%;
    height: 100%;
  }
  .contact-block {
    position: absolute;
    right: 92px;
    top: 70px;
    text-align: right;
    color: var(--contact-text);
    font-size: 29px;
    font-style: normal;
    font-weight: 400;
    line-height: 43px;
    letter-spacing: 0.2px;
    white-space: nowrap;
  }
  .brand-name {
    position: absolute;
    left: 110px;
    top: 400px;
    font-size: 150px;
    font-weight: 700;
    line-height: 1;
    color: var(--brand-text);
    letter-spacing: 2px;
  }
  .person-name {
    position: absolute;
    right: 96px;
    top: 490px;
    font-size: 41px;
    font-weight: 600;
    line-height: 1;
    color: var(--name-text);
    white-space: nowrap;
  }
</style>
</head>
<body>
  <div class="business-card">
    <div class="card-face">
      <svg class="header-band" viewBox="0 0 1176 679" preserveAspectRatio="none" aria-hidden="true">
        <defs>
          <linearGradient id="bandGradient" x1="0" y1="1" x2="1" y2="0">
            <stop offset="0" stop-color="var(--band-deep)"/>
            <stop offset="0.55" stop-color="var(--band-mid)"/>
            <stop offset="1" stop-color="var(--band-light)"/>
          </linearGradient>
          <linearGradient id="swooshGradient" x1="0" y1="0" x2="1" y2="0">
            <stop offset="0" stop-color="var(--swoosh-dark)"/>
            <stop offset="0.3" stop-color="var(--swoosh-light)"/>
            <stop offset="0.65" stop-color="var(--swoosh-dark)"/>
            <stop offset="1" stop-color="var(--swoosh-light)"/>
          </linearGradient>
        </defs>
        <path d="M0,0 H1176 V318 C1080,345 1000,356 900,346 C760,332 560,226 380,224 C250,222 120,276 0,298 Z" fill="url(#bandGradient)"/>
        <path d="M0,298 C120,276 250,222 380,224 C560,226 760,332 900,346 C1000,356 1080,345 1176,318 L1176,334 C1080,362 1000,372 900,362 C760,348 560,244 380,242 C250,240 120,294 0,314 Z" fill="url(#swooshGradient)"/>
      </svg>

      <address class="contact-block">
        <div class="contact-line">418B Quarry Gate Rd, Harlow Point, MD 21870</div>
        <div class="contact-line">Cell: 443-555-0184 | Phone: 410-555-0127</div>
        <div class="contact-line">Fax: 410-555-0139</div>
        <div class="contact-line">Email: lou@drkhvc.com | www.drkhvc.com</div>
      </address>

      <div class="brand-name">DRK</div>

      <div class="person-name">Lou Ferrand</div>
    </div>
  </div>
</body>
</html>
```